Pier Grove Profile Bacground Needed

I need a simple Pier Grove Background graphic for my Pier Grove profile. My website is www.MeridelVKP.com
I have attached a couple of photos and our logo.

The tag line is: BEAUTY | FUNCTION | ON TIME | ON BUDGET

```html
<!DOCTYPE html>
<html lang="en">
<head>
<meta charset="utf-8">
<title>Meridel Kitchen &amp; Bath – Pier Grove Banner</title>
<link href="https://fonts.googleapis.com/css2?family=Jost:wght@700&family=Libre+Caslon+Text:wght@700&display=swap" rel="stylesheet">
<style>
  :root {
    --ink: #141414;
    --tile-light: #eef4f7;
    --tile-mid: #d9e7ee;
    --tile-blue: #c3d9e4;
    --sky: #bcd8ea;
    --sea: #7fb7c9;
    --wall-blue: #a9c8d6;
    --porcelain: #f6f6f4;
    --floor: #e3dfda;
  }
  * { margin: 0; padding: 0; box-sizing: border-box; }
  html, body { width: 1200px; height: 300px; overflow: hidden; background: var(--tile-light); }
  .banner {
    position: relative;
    width: 1200px;
    height: 300px;
    overflow: hidden;
    background: linear-gradient(135deg, var(--tile-light) 0%, var(--tile-mid) 45%, var(--tile-light) 70%, var(--tile-blue) 100%);
  }
  .bathroom-photo {
    position: absolute;
    left: 0; top: 0;
    width: 780px; height: 300px;
    background: linear-gradient(180deg, var(--sky) 0%, #dfeaf2 30%, var(--sea) 45%, #9fbf8f 55%, var(--wall-blue) 62%, var(--porcelain) 75%, var(--floor) 100%);
    -webkit-mask-image: linear-gradient(90deg, #000 0%, #000 72%, transparent 100%);
    mask-image: linear-gradient(90deg, #000 0%, #000 72%, transparent 100%);
  }
  .brand-name {
    position: absolute;
    left: 760px; top: 112px;
    width: 374px;
    text-align: center;
    font-family: 'Libre Caslon Text', serif;
    font-weight: 700;
    font-size: 28px;
    line-height: 1.2;
    color: var(--ink);
    white-space: nowrap;
  }
  .tagline {
    position: absolute;
    left: 720px; top: 218px;
    width: 452px;
    text-align: center;
    font-family: 'Libre Caslon Text', serif;
    font-weight: 700;
    font-size: 16px;
    letter-spacing: 1.2px;
    color: var(--ink);
    white-space: nowrap;
  }
  .website {
    position: absolute;
    left: 846px; top: 264px;
    width: 200px;
    text-align: center;
    font-family: 'Jost', sans-serif;
    font-weight: 700;
    font-size: 14px;
    letter-spacing: 1.3px;
    color: var(--ink);
    white-space: nowrap;
  }
</style>
</head>
<body>
  <div class="banner">
    <div class="bathroom-photo" role="img" aria-label="Bright coastal bathroom with white vanities, blue glass tile walls, a freestanding tub and tall windows looking out to palm trees and the ocean"></div>

    <p class="brand-name">Meridel Kitchen &amp; Bath</p>

    <p class="tagline">BEAUTY | FUNCTION | ON TIME | ON BUDGET</p>
    <p class="website">www.MeridelVKP.com</p>
  </div>
</body>
</html>
```